CraneHollow - Business Card and Letterhead

After having received some fantastic submissions in our recent logo design project, I would now like to extend our branding to letterheads and business cards.
CraneHollow is a consulting service in the Construction Industry. We deal with both residential and commercial projects, and our clients include Architects, Builders, Tradespeople and Home Owners.
The designs should be simple and effective, convey personal service and professionalism, and display some level of creativity.
For both the business cards and letterhead, a white card stock will be used. This project is for business cards and letterheads only. Our new logo is attached for use.
The designs should incorporate our two main colours which are Blue (RGB 14,92,143) and Green (RGB 132,194,37).
For the time being, please submit all designs showing generic information including name, mobile number, email, postal address and website details. No fax number or physical address is required. I will provide our actual contact details once a final design has been selected.
I encourage you to interpret this brief in your own creative way, and look forward to some quality submissions.
Thanks!
Leo
CraneHollow.

```html
<!DOCTYPE html>
<html lang="en">
<head>
<meta charset="utf-8">
<title>CraneHollow Letterhead</title>
<link rel="stylesheet" href="https://fonts.googleapis.com/css2?family=Source+Sans+3:wght@400;700&display=swap">
<style>
  :root {
    --brand-blue: #0e5c8f;
    --brand-green: #84c225;
    --wash: #f4f8fd;
    --paper: #ffffff;
    --ink: #2b3650;
    --mail: #8dbd5c;
  }
  html, body {
    margin: 0;
    padding: 0;
    overflow: hidden;
    background: var(--paper);
  }
  .letterhead {
    position: relative;
    width: 848px;
    height: 1200px;
    overflow: hidden;
    background: var(--paper);
    font-family: "Source Sans 3", sans-serif;
  }
  .backdrop {
    position: absolute;
    inset: 0;
  }
  .brand {
    position: absolute;
    left: 74px;
    top: 62px;
    display: flex;
    align-items: center;
    gap: 12px;
  }
  .brand-name {
    font-size: 40px;
    font-weight: 700;
    color: var(--brand-blue);
    letter-spacing: -0.5px;
  }
  .brand-square {
    width: 30px;
    height: 30px;
    background: var(--brand-green);
  }
  .contact {
    position: absolute;
    left: 0;
    right: 0;
    top: 1098px;
    text-align: center;
    font-size: 16.5px;
    line-height: 22px;
    color: var(--ink);
  }
  .contact-mail {
    color: var(--mail);
  }
</style>
</head>
<body>
  <main class="letterhead">
    <svg class="backdrop" width="848" height="1200" viewBox="0 0 848 1200" aria-hidden="true">
      <circle cx="660" cy="445" r="632" fill="var(--wash)"/>
    </svg>

    <header class="brand">
      <span class="brand-name">CraneHollow</span>
      <span class="brand-square"></span>
    </header>

    <footer class="contact">
      <div class="contact-line">No.12, Harbour Lane, West Quarter, Riverton, India- 600123 Ph: +91 0400 5550147 ,Mob: +91 9000055501</div>
      <div class="contact-mail">e-mail: hello@cranehollow.example</div>
    </footer>
  </main>
</body>
</html>
```